Lorvan Carry Nutrition Funnel Pouch & Cap Pouch

The Funnel Pouch (without cap), Funnel Pouch (with cap), and Box will be using the same design and style, expect a few small changes for each.

Funnel Pouch (one time use)
1. Design for front and back of a Funnel Pouch & With Cap Funnel Pouch
2. Attached are the design requirements and photo of products

Funnel Pouch (Reusable)
3. this is the product WITH cap
4. the only difference in this design is that
"Spin n' Seal Cap" and "Reusable" need to be added somewhere on fron and back
- but overall it is the same design as the funnel pouch with no cap

After design is completed,
5. Professional white background image of both Funnel pouches

I have attached some examples of other products where you can get some ideas.
Updates

I am looking for a professional designer who I plan to work with long term for multiple projects. Please submit soon, thanks! Added Friday, April 7, 2017

Target Market(s)

health/ fitness enthusiasts, outdoor market, on the go indivudals, gym goers, Tamsel Sports and Outdoors, Brindle Market

Industry/Entity Type

Supplement

Requirements
Must have
• Professional, creative design that follows basic requirements.
Nice to have
• incorporate LORVAN because that is our company logo name.
Should not have
• Should not be a design that I can easily make myself.

```html
<!DOCTYPE html>
<html lang="en">
<head>
<meta charset="utf-8">
<title>Lorvan Carry Nutrition – Funnel Pouch</title>
<link href="https://fonts.googleapis.com/css2?family=Montserrat:wght@700;800&display=swap" rel="stylesheet">
<style>
  :root {
    --backdrop: #e6e6e6;
    --kraft: #c9b47f;
    --kraft-dark: #b29c66;
    --silver: #dcdcdc;
    --brand-red: #8e0c0c;
    --ink: #141414;
    --mix-tone: #9c8470;
  }
  html, body {
    margin: 0;
    padding: 0;
    width: 1200px;
    height: 858px;
    overflow: hidden;
    background: var(--backdrop);
  }
  .pouch-art {
    display: block;
    width: 1200px;
    height: 858px;
  }
  .brand-name {
    font-family: "Montserrat", sans-serif;
    font-weight: 800;
    font-size: 30px;
    letter-spacing: 1px;
    fill: var(--brand-red);
  }
  .tagline {
    font-family: "Montserrat", sans-serif;
    font-weight: 700;
    font-size: 15px;
    fill: var(--ink);
  }
  .step-label {
    font-family: "Montserrat", sans-serif;
    font-weight: 700;
    font-size: 14px;
    fill: var(--ink);
  }
  .pouch-body { fill: var(--kraft); }
  .seal-stripe { stroke: var(--kraft-dark); stroke-width: 1.4; }
  .brand-rule { stroke: var(--brand-red); stroke-width: 3; }
  .window-panel { fill: var(--silver); }
  .kraft-band { fill: var(--kraft); }
  .usage-illustration { fill: var(--mix-tone); }
  .dispense-arrow { fill: var(--brand-red); }
</style>
</head>
<body>
<svg class="pouch-art" viewBox="0 0 1200 858" xmlns="http://www.w3.org/2000/svg">
  <!-- pouch silhouette -->
  <polygon class="pouch-body" points="475,160 725,160 655,665 545,665"/>

  <!-- crimped top seal -->
  <g class="top-seal">
    <line class="seal-stripe" x1="476" y1="166" x2="724" y2="166"/>
    <line class="seal-stripe" x1="476" y1="171" x2="724" y2="171"/>
    <line class="seal-stripe" x1="476" y1="176" x2="723" y2="176"/>
    <line class="seal-stripe" x1="477" y1="181" x2="723" y2="181"/>
    <line class="seal-stripe" x1="477" y1="186" x2="722" y2="186"/>
    <line class="seal-stripe" x1="478" y1="191" x2="722" y2="191"/>
    <line class="seal-stripe" x1="478" y1="196" x2="721" y2="196"/>
  </g>

  <!-- brand block -->
  <text class="brand-name" x="600" y="234" text-anchor="middle">LORVAN</text>
  <line class="brand-rule" x1="486" y1="248" x2="714" y2="248"/>
  <text class="tagline" x="600" y="268" text-anchor="middle">CARRY NUTRITION</text>
  <line class="brand-rule" x1="488" y1="278" x2="712" y2="278"/>

  <!-- silver window -->
  <polygon class="window-panel" points="504,284 696,284 648,655 552,655"/>
  <polygon class="kraft-band" points="520,568 680,568 677,592 523,592"/>
  <rect class="kraft-band" x="584" y="592" width="32" height="0"/>

  <!-- usage steps -->
  <text class="step-label" x="685" y="305" text-anchor="end">LOAD YOUR</text>
  <text class="step-label" x="685" y="326" text-anchor="end">MIX</text>

  <g class="usage-illustration" role="img" aria-label="Illustration: scoop pouring powder mix into a funnel that dispenses into a bottle">
    <rect x="520" y="332" width="155" height="140" rx="6"/>
    <rect x="614" y="476" width="30" height="72" rx="5"/>
  </g>

  <text class="step-label" x="571" y="488" text-anchor="middle">DISPENSE</text>
  <text class="step-label" x="571" y="507" text-anchor="middle">ANYTIME</text>
  <text class="step-label" x="571" y="526" text-anchor="middle">INTO</text>
  <text class="step-label" x="571" y="545" text-anchor="middle">ANY</text>
  <text class="step-label" x="571" y="564" text-anchor="middle">BOTTLE</text>

  <!-- dispense arrow -->
  <polygon class="dispense-arrow" points="589,572 611,572 611,630 630,630 600,660 570,630 589,630"/>
</svg>
</body>
</html>
```